Morvela Aesthetic Doctor

I require an elegant, luxurious looking business card for my aesthetic business. I am a doctor and that will set me aside from competitors. I am planning to provide home and spa based treatments to clients with high expectations. I have attached my logo.

```html
<!DOCTYPE html>
<html lang="en">
<head>
<meta charset="utf-8">
<title>Morvela Aesthetic Doctor – Business Card</title>
<link rel="stylesheet" href="https://fonts.googleapis.com/css2?family=Work+Sans:wght@400;500&display=swap">
<style>
  :root {
    --backdrop: #161616;
    --card: #242424;
    --card-edge: #2e2e2e;
    --ink: #f2f2f2;
    --silver: #c9c9c9;
    --accent: #1ea7e8;
    --mark: #3a3a3a;
  }
  * { box-sizing: border-box; margin: 0; padding: 0; }
  html, body {
    width: 1200px; height: 900px; overflow: hidden;
    background: var(--backdrop);
    font-family: "Work Sans", sans-serif;
    color: var(--ink);
  }
  .sheet {
    width: 1200px; height: 900px;
    display: flex; flex-direction: column; align-items: center; justify-content: center;
    gap: 40px;
  }
  .card {
    position: relative;
    width: 700px; height: 400px;
    background: linear-gradient(135deg, var(--card) 0%, var(--card-edge) 100%);
    box-shadow: 0 10px 30px rgba(0,0,0,.55);
  }

  /* Front */
  .card--front { display: flex; flex-direction: column; align-items: center; justify-content: center; }
  .brand { display: flex; align-items: center; gap: 22px; margin-bottom: 44px; }
  .brand__circle { width: 78px; height: 78px; border-radius: 50%; border: 2px solid var(--mark); }
  .brand__name {
    font-size: 34px; font-weight: 400; letter-spacing: 4px; line-height: 1.15;
    color: var(--silver); text-transform: uppercase;
  }
  .services { text-align: center; font-size: 17px; letter-spacing: 1.6px; line-height: 1.6; }
  .services .sep { color: var(--accent); margin: 0 6px; }

  /* Back */
  .card--back { padding: 0 56px; }
  .back__main {
    position: absolute; left: 56px; right: 56px; top: 150px;
    display: flex; align-items: center; justify-content: center; gap: 34px;
  }
  .person { text-align: right; }
  .person__name { color: var(--accent); font-size: 22px; font-weight: 500; margin-bottom: 6px; }
  .person__credential { font-size: 19px; letter-spacing: 1.4px; line-height: 1.3; }
  .divider { width: 2px; height: 86px; background: var(--accent); }
  .contact { list-style: none; font-size: 19px; letter-spacing: 1.4px; line-height: 1.45; }
  .contact li { display: flex; align-items: center; gap: 10px; }
  .contact svg { width: 14px; height: 14px; flex: none; }
  .tagline {
    position: absolute; left: 0; right: 0; bottom: 58px; text-align: center;
    font-size: 19px; letter-spacing: 2.6px; text-transform: uppercase;
  }
</style>
</head>
<body>
<main class="sheet">
  <section class="card card--front">
    <div class="brand">
      <span class="brand__circle"></span>
      <p class="brand__name">Morvela<br>Aesthetic Doctor</p>
    </div>
    <p class="services">
      Dermal injectables<span class="sep">|</span>Plasma facials<span class="sep">|</span>Microneedling<br>
      Skin boosters<span class="sep">|</span>Excessive sweating
    </p>
  </section>

  <section class="card card--back">
    <div class="back__main">
      <div class="person">
        <p class="person__name">Dr Elsa Vantrell MRCPCH MD</p>
        <p class="person__credential">Australasian Diploma<br>of Aesthetic Medicine</p>
      </div>
      <span class="divider"></span>
      <ul class="contact">
        <li>
          <svg viewBox="0 0 16 16" fill="none" stroke="var(--accent)" stroke-width="1.6"><path d="M4 1.5l2.5 3-1.5 1.5c.8 2 2.5 3.7 4.5 4.5l1.5-1.5 3 2.5-1.5 2.5C7 13.5 2.5 9 1.5 3z"/></svg>
          0800 454 918
        </li>
        <li>
          <svg viewBox="0 0 16 16" fill="none" stroke="var(--accent)" stroke-width="1.4"><rect x="1.5" y="3.5" width="13" height="9"/><path d="M1.5 3.5L8 9l6.5-5.5"/></svg>
          elsa@morvela.co.nz
        </li>
        <li>
          <svg viewBox="0 0 16 16" fill="none" stroke="var(--accent)" stroke-width="1.2"><circle cx="8" cy="8" r="6.5"/><ellipse cx="8" cy="8" rx="3" ry="6.5"/><path d="M1.5 8h13M2.5 4.8h11M2.5 11.2h11"/></svg>
          www.morvela.co.nz
        </li>
      </ul>
    </div>
    <p class="tagline">Home and spa based treatments</p>
  </section>
</main>
</body>
</html>
```